Business Card Design Project

I need a business card design for an Organic drive thru coffee kiosk. We will serve organic coffee, teas & smoothies and will serve healthy breakfast food/snacks for people on the go.
I want the card to have 2-3 colors max (earthy colors like browns, greens and so on).
I have attached the logo I want used and would love to play off the theme of "balance."
Include:
Sun-Grove Coffee
address: 4170 Pelham Ct. Raleigh, NC 27593
phone: 919-307-4462
website: www.sun-grove-example.com (website is not up yet but still include it on card)
email: Dorothy@sun-grove-example.com
I want one of the following sayings somewhere on the card (the front or back is fine):
"Eat & Drink Well, on the run!"
"Break the fast with Sun-Grove"
Maybe on the back list what we offer:
-Organic coffee, espresso & tea
-Blendora smoothies & protein shakes
-Zesty Tonic (100% fresh local fruit and veggies)
-Healthy Bites

```html
<!DOCTYPE html>
<html lang="en">
<head>
<meta charset="utf-8">
<title>Sun-Grove Coffee – Business Cards</title>
<link href="https://fonts.googleapis.com/css2?family=Vollkorn:ital,wght@0,400;0,700;1,700&family=Archivo:wght@400&display=swap" rel="stylesheet">
<style>
  :root {
    --espresso: #2e1a0f;
    --roast: #7a2818;
    --leaf: #3d4a12;
    --card-edge: #9aa3a3;
    --paper: #ffffff;
  }
  * { box-sizing: border-box; margin: 0; padding: 0; }
  html, body { width: 1200px; height: 1000px; overflow: hidden; background: var(--paper); }
  .stage { position: relative; width: 1200px; height: 1000px; }

  /* Brand lockup behind the cards */
  .brand-dot {
    position: absolute; left: 485px; top: 215px;
    width: 240px; height: 240px; border-radius: 50%;
    background: var(--roast);
  }
  .brand-name {
    position: absolute; left: 232px; top: 488px;
    font-family: "Vollkorn", serif; font-weight: 400;
    font-size: 164px; line-height: 1; color: var(--espresso);
    letter-spacing: -2px; white-space: nowrap;
  }
  .brand-tagline {
    position: absolute; left: 290px; top: 676px;
    font-family: "Archivo", sans-serif; font-size: 40px;
    letter-spacing: 9px; color: var(--roast); white-space: nowrap;
  }

  /* Cards */
  .card {
    position: absolute; width: 475px; height: 271px;
    background: var(--paper); border: 1px solid var(--card-edge);
    box-shadow: 3px 4px 6px rgba(0,0,0,.35);
    font-family: "Vollkorn", serif; overflow: hidden;
  }
  .card--back-top { left: 105px; top: 52px; }
  .card--front-top { left: 60px; top: 204px; }
  .card--front-bottom { left: 660px; top: 527px; }
  .card--back-bottom { left: 615px; top: 663px; }

  /* Front side */
  .front__mark {
    position: absolute; left: 40px; top: 40px; width: 180px;
    text-align: center;
  }
  .front__dot {
    width: 100px; height: 100px; border-radius: 50%;
    background: var(--roast); margin: 0 auto 14px;
  }
  .front__name {
    font-weight: 700; font-size: 24px; color: var(--espresso);
  }
  .front__divider {
    position: absolute; left: 238px; top: 24px; width: 2px; height: 234px;
    background: var(--espresso);
  }
  .front__contact {
    position: absolute; left: 250px; top: 42px; width: 196px;
    text-align: center; color: var(--leaf);
    font-size: 13.5px; letter-spacing: 1px; line-height: 18px;
  }
  .front__company {
    font-weight: 700; font-size: 16px; color: var(--espresso);
    letter-spacing: .5px; margin-bottom: 1px;
  }
  .front__label {
    font-weight: 700; font-size: 11.5px; color: var(--leaf);
    margin-top: 15px; line-height: 14px;
  }
  .front__value { font-size: 12.5px; line-height: 16px; }
  .front__tagline {
    position: absolute; left: 0; width: 476px; top: 236px;
    text-align: center; font-family: "Archivo", sans-serif;
    font-size: 18px; letter-spacing: 3px; color: var(--roast);
  }

  /* Back side */
  .back__frame { position: absolute; inset: 0; }
  .back__offer {
    position: absolute; font-size: 13px; letter-spacing: 1px;
    color: var(--leaf); white-space: nowrap; line-height: 1;
  }
  .back__offer--top { left: 40px; top: 19px; display: flex; align-items: center; }
  .back__offer--bottom { left: 46px; top: 239px; }
  .back__offer--left {
    left: 25px; top: 134px; transform: translate(-50%, -50%) rotate(-90deg);
  }
  .back__offer--right {
    left: 452px; top: 137px; transform: translate(-50%, -50%) rotate(90deg);
  }
  .back__bullet {
    display: inline-block; width: 10px; height: 12px; border-radius: 50%;
    background: var(--roast); margin: 0 2px;
  }
  .back__dash { display: inline-block; width: 5px; height: 1.5px; background: var(--espresso); }
  .back__slogan {
    position: absolute; left: 0; width: 475px; top: 126px; text-align: center;
  }
  .back__slogan span {
    font-weight: 700; font-style: italic; font-size: 15.5px;
    letter-spacing: 1.2px; color: var(--roast);
    border-bottom: 1.5px solid var(--leaf); padding: 0 1px 1px;
  }
</style>
</head>
<body>
<main class="stage">
  <div class="brand-dot"></div>
  <div class="brand-name">Sun-Grove</div>
  <div class="brand-tagline">ORGANIC COFFEE + CAFE</div>

  <!-- back card (upper) -->
  <section class="card card--back-top">
    <svg class="back__frame" width="475" height="271" viewBox="0 0 475 271">
      <g fill="none" stroke="var(--espresso)" stroke-width="1.5">
        <path d="M36 26 H23 V38"/>
        <path d="M23 230 V246 H40"/>
        <path d="M431 26 H451 V52"/>
        <path d="M451 220 V246 H434"/>
      </g>
      <g fill="var(--roast)">
        <ellipse cx="23" cy="46" rx="5" ry="6"/>
        <ellipse cx="23" cy="222" rx="5" ry="6"/>
        <ellipse cx="451" cy="61" rx="5" ry="6"/>
        <ellipse cx="451" cy="210" rx="5" ry="6"/>
      </g>
    </svg>
    <p class="back__offer back__offer--top">Organic coffee, espresso &amp; tea<span class="back__dash"></span><span class="back__bullet"></span><span class="back__dash"></span>Healthy bites</p>
    <p class="back__offer back__offer--left">Blendora Smoothies</p>
    <p class="back__offer back__offer--right">Protein Shakes</p>
    <p class="back__offer back__offer--bottom">Zesty Tonic(100% fresh local fruit and veggies)</p>
    <p class="back__slogan"><span>EAT &amp; DRINK WELL, ON THE RUN!</span></p>
  </section>

  <!-- front card (upper) -->
  <section class="card card--front-top">
    <div class="front__mark">
      <div class="front__dot"></div>
      <p class="front__name">Sun-Grove</p>
    </div>
    <div class="front__divider"></div>
    <div class="front__contact">
      <p class="front__company">Sun-Grove Coffee</p>
      <p>4170 Pelham Ct.</p>
      <p>Raleigh, NC 27593</p>
      <p>919-307-4462</p>
      <p class="front__label">website:</p>
      <p class="front__value">www.sun-grove-example.com</p>
      <p class="front__label">email:</p>
      <p class="front__value">Dorothy@sun-grove-example.com</p>
    </div>
    <p class="front__tagline">ORGANIC COFFEE + CAFE</p>
  </section>

  <!-- front card (lower) -->
  <section class="card card--front-bottom">
    <div class="front__mark">
      <div class="front__dot"></div>
      <p class="front__name">Sun-Grove</p>
    </div>
    <div class="front__divider"></div>
    <div class="front__contact">
      <p class="front__company">Sun-Grove Coffee</p>
      <p>4170 Pelham Ct.</p>
      <p>Raleigh, NC 27593</p>
      <p>919-307-4462</p>
      <p class="front__label">website:</p>
      <p class="front__value">www.sun-grove-example.com</p>
      <p class="front__label">email:</p>
      <p class="front__value">Dorothy@sun-grove-example.com</p>
    </div>
    <p class="front__tagline">ORGANIC COFFEE + CAFE</p>
  </section>

  <!-- back card (lower) -->
  <section class="card card--back-bottom">
    <svg class="back__frame" width="475" height="271" viewBox="0 0 475 271">
      <g fill="none" stroke="var(--espresso)" stroke-width="1.5">
        <path d="M36 26 H23 V38"/>
        <path d="M23 230 V246 H40"/>
        <path d="M431 26 H451 V52"/>
        <path d="M451 220 V246 H434"/>
      </g>
      <g fill="var(--roast)">
        <ellipse cx="23" cy="46" rx="5" ry="6"/>
        <ellipse cx="23" cy="222" rx="5" ry="6"/>
        <ellipse cx="451" cy="61" rx="5" ry="6"/>
        <ellipse cx="451" cy="210" rx="5" ry="6"/>
      </g>
    </svg>
    <p class="back__offer back__offer--top">Organic coffee, espresso &amp; tea<span class="back__dash"></span><span class="back__bullet"></span><span class="back__dash"></span>Healthy bites</p>
    <p class="back__offer back__offer--left">Blendora Smoothies</p>
    <p class="back__offer back__offer--right">Protein Shakes</p>
    <p class="back__offer back__offer--bottom">Zesty Tonic(100% fresh local fruit and veggies)</p>
    <p class="back__slogan"><span>EAT &amp; DRINK WELL, ON THE RUN!</span></p>
  </section>
</main>
</body>
</html>
```